Business Card design for construction company

I would like a business card design for a construction company - Harlow Constructions. I have attached the ai logo file for use. I would like the card to be very smart and clean and incorporate only white and the two colours in the logo. I would like the card to have two sides. One side can just have the logo, the other with the relevant information.

Target Market(s)

Building and Construction Clients

Industry/Entity Type

Business

Contact Information for Business Card

Name: Tom Pardoe
Company: Harlow Constructions Pty Limited
Address: 14 Mallee Crescent Carrow Vale 2093
Phone: 0427 531 068
Email: tomp@harlowbuild-example.com.au

Font styles to use
Serif
Sans Serif

Requirements
Must have
• Details noted above
• Logo as provided
• Colours as in logo
• Square edges
• A font that compliments the logo
Should not have
• Any colour other than white and those in logo
• Rounded edges

```html
<!DOCTYPE html>
<html lang="en">
<head>
<meta charset="utf-8">
<title>Harlow Constructions — Business Card</title>
<link rel="stylesheet" href="https://fonts.googleapis.com/css2?family=Michroma&family=Work+Sans:wght@300;400&display=swap">
<style>
  :root {
    --backdrop: #1d1d1e;
    --card: #141415;
    --card-edge: #1b1b1c;
    --emboss: #404042;
    --emboss-dark: #070707;
    --silver: #b9b9bb;
    --rule: #4a4a4c;
  }
  * { margin: 0; padding: 0; box-sizing: border-box; }
  html, body {
    width: 1200px; height: 900px; overflow: hidden;
    background: var(--backdrop);
  }
  .sheet {
    width: 1200px; height: 900px;
    display: flex; flex-direction: column; align-items: center; justify-content: center;
    gap: 48px;
  }
  .card {
    position: relative;
    width: 640px; height: 372px;
    background: linear-gradient(160deg, var(--card-edge) 0%, var(--card) 55%, #19191a 100%);
    box-shadow: 0 14px 30px rgba(0,0,0,0.55);
  }

  /* Front */
  .card-front { display: flex; align-items: center; justify-content: center; }
  .company-name {
    font-family: "Work Sans", sans-serif;
    font-weight: 300;
    font-size: 24px;
    color: var(--silver);
  }

  /* Back */
  .identity {
    position: absolute; left: 40px; top: 148px;
    width: 236px; text-align: right;
  }
  .identity-name {
    font-family: "Michroma", sans-serif;
    font-size: 19px;
    letter-spacing: 1.5px;
    text-transform: uppercase;
    color: var(--emboss);
    text-shadow: 0 -1px 0 var(--emboss-dark);
    white-space: nowrap;
  }
  .identity-role {
    font-family: "Work Sans", sans-serif;
    font-weight: 400;
    font-size: 13px;
    margin-top: 3px;
    color: var(--emboss);
    text-shadow: 0 -1px 0 var(--emboss-dark);
  }
  .divider {
    position: absolute; left: 298px; top: 140px;
    width: 1px; height: 76px;
    background: var(--rule);
  }
  .contact {
    position: absolute; left: 318px; top: 138px;
    font-family: "Work Sans", sans-serif;
    font-weight: 300;
    font-size: 15px;
    line-height: 21px;
    letter-spacing: 0.4px;
    color: var(--silver);
    list-style: none;
  }
  .contact li { display: flex; align-items: center; gap: 8px; white-space: nowrap; }
  .contact .plain { padding-left: 18px; }
  .contact svg { width: 10px; height: 10px; flex: none; }
</style>
</head>
<body>
<main class="sheet">

  <section class="card card-front" aria-label="Card front">
    <div class="company-name">Harlow Constructions</div>
  </section>

  <section class="card card-back" aria-label="Card back">
    <div class="identity">
      <div class="identity-name">Tom Pardoe</div>
      <div class="identity-role">President</div>
    </div>
    <div class="divider"></div>
    <ul class="contact">
      <li class="plain">14 Mallee Crescent</li>
      <li class="plain">Carrow Vale 2093</li>
      <li>
        <svg viewBox="0 0 10 10" aria-hidden="true"><path d="M2 0.8 L3.6 0.8 L4.2 3 L3.1 3.8 Q4 6 6.2 6.9 L7 5.8 L9.2 6.4 L9.2 8 Q9 9.4 7.4 9.2 Q1.2 8.2 0.8 2.6 Q0.8 1 2 0.8 Z" fill="#b9b9bb"/></svg>
        0427 531 068
      </li>
      <li>
        <svg viewBox="0 0 10 10" aria-hidden="true"><rect x="0.6" y="1.8" width="8.8" height="6.4" fill="none" stroke="#b9b9bb" stroke-width="1"/><path d="M0.8 2.2 L5 5.4 L9.2 2.2" fill="none" stroke="#b9b9bb" stroke-width="1"/></svg>
        tomp@harlowbuild-example.com.au
      </li>
    </ul>
  </section>

</main>
</body>
</html>
```